IT Services company needs a postcard.

Goal - Introduce customers to Lantern Host and promote our Lantern Host's services driving customers to the website.
Audience - Programmers/developers/designers/IT Professionals
Overview - Lantern Host is an Internet solution company in Northern California that provides reliable IT infrastructure to businesses of all sizes. We provide competitively priced enterprise-grade dedicated servers, private clouds, and colocation solutions
Design - Match www.lanternhost-example.com. To be mailed in US, must meet USPS requirements. http://qvbrandworks-example.com/projects/Postcard_Oversize.jpg
Lantern Host Logo: http://www.lanternhost-example.com/lanternhost/logo.psd

Attached are rough samples that I put together. These are just an idea of layouts that I would like. If you can make thing better, go with it. If the images don't work for print, let me know (I don't have hi-res images). If it needs something added, let me know. If it needs something taken off, let me know. I'm not an artist or marekting professional and I'm looking for a design to meet my goals. Change colors, fonts, layout,... wow me.

Front
Look to match first frame at http://www.lanternhost-example.com with rack of servers on the left
Text to include
- Headline: Lantern Host
- Your IT Infrastructure Partner
- Offer: Dedicated Server
- Dual E5-2620V2
- 16G RAM
- 2X250GB Drives
- 100Mbps
$339/mo
- Contact information
- www.lanternhost-example.com
- sales@lanternhost-example.com
- (888) 555-0142

Back
- Delta Vault Center (Featured section)
- Use images/text from right side of http://www.lanternhost-example.com/colocation/ to highlight that we are a high quality datacenter in Sacramento. Want customers to know that we are a local company.
- Private Cloud Server (minor section)
- 24 VCPUs
- 32 GB RAM
- 1TB RAID10 Storage
- 100Mbps
- $539/mo
- Colocation (minor section)
- Space - 1U
- Power - 1A@208V
- Public Network - 100Mbps
- Private Network - 1Gbps
- $89/mo

Target Market(s)

Programmers/developers/designers/IT Professionals

Industry/Entity Type

It Company

Requirements
Must have
• Design to match www.lanternhost-example.com

```html
<!DOCTYPE html>
<html lang="en">
<head>
<meta charset="utf-8">
<title>Lantern Host – Postcard Back</title>
<link rel="stylesheet" href="https://fonts.googleapis.com/css2?family=Roboto+Condensed:ital,wght@0,500;0,700;1,700&display=swap">
<style>
  :root {
    --page: #ffffff;
    --card-dark: #c9c9cb;
    --card-light: #ffffff;
    --ink: #4a4a4c;
    --band: #353436;
    --band-edge: #2a292b;
    --white: #ffffff;
    --orange: #f28a3a;
    --green: #7cc242;
    --brand-green: #2e8a3a;
    --tile-dark: #333335;
    --stamp-line: #c8c8c8;
  }
  * { box-sizing: border-box; margin: 0; padding: 0; }
  html, body { width: 1200px; height: 1000px; overflow: hidden; background: var(--page); }
  body { position: relative; font-family: "Roboto Condensed", "Arial Narrow", sans-serif; }

  .postcard {
    position: absolute; left: 43px; top: 80px; width: 1122px; height: 728px;
    background: linear-gradient(115deg, var(--card-dark) 0%, #e2e2e3 45%, var(--card-light) 70%, var(--card-light) 100%);
    overflow: hidden;
  }
  .postcard > * { position: absolute; }

  .stamp-box { left: 937px; top: 20px; width: 160px; height: 160px; border: 1px solid var(--stamp-line); }

  .headline {
    left: 50px; top: 54px; font-size: 38px; font-weight: 700; color: var(--ink);
    letter-spacing: 0.5px; line-height: 1;
  }

  .brand { left: 522px; top: 44px; display: flex; align-items: center; gap: 14px; }
  .brand-dot { width: 50px; height: 50px; border-radius: 50%; background: var(--brand-green); }
  .brand-name { font-size: 38px; font-weight: 700; color: var(--orange); letter-spacing: 1px; line-height: 1; }

  .tiles { left: 47px; top: 120px; display: flex; gap: 24px; }
  .tile { width: 155px; height: 138px; border-radius: 6px; border: 2px solid #e6e6e6; }
  .tile--aisle { background: linear-gradient(160deg, #b89ac8, #6e4f6a 55%, #c07040); }
  .tile--racks { background: linear-gradient(170deg, #c9b3d6, #8f7a8e 55%, #5a5048); }
  .tile--cabling { background: linear-gradient(120deg, #3a3a3a, #b9b9b3 50%, #d8d8d0); }
  .tile--scanner { background: linear-gradient(140deg, #5f6b6a, #2c3433 60%, #8a3a2a); }
  .tile--support {
    background: var(--tile-dark); color: var(--white); display: flex; flex-direction: column;
    align-items: center; justify-content: center; font-weight: 700; line-height: 0.95;
  }
  .tile--support .big { font-size: 60px; }
  .tile--support .small { font-size: 33px; }

  .features { left: 48px; font-size: 24px; font-weight: 700; color: var(--ink); display: flex; align-items: center; letter-spacing: 0.5px; }
  .features--one { top: 277px; }
  .features--two { top: 325px; }
  .features .sep { width: 2px; height: 38px; background: var(--orange); margin: 0 8px; }

  .offers-band { left: 0; top: 372px; width: 745px; height: 258px; }

  .offer { top: 420px; width: 360px; text-align: center; color: var(--white); }
  .offer--cloud { left: 0; width: 352px; }
  .offer--colo { left: 364px; width: 360px; }
  .offer-title { font-size: 19px; font-weight: 700; font-style: italic; color: var(--green); margin-bottom: 10px; }
  .offer-spec { font-size: 22px; font-weight: 700; line-height: 32px; display: flex; justify-content: center; align-items: center; }
  .offer-spec .sep { width: 2px; height: 26px; background: var(--orange); margin: 0 9px; }
  .offer-price { font-size: 32px; font-weight: 700; font-style: italic; color: var(--orange); margin-top: 12px; }
</style>
</head>
<body>
  <section class="postcard" aria-label="Lantern Host postcard back">
    <div class="stamp-box" aria-label="Postage area"></div>

    <h1 class="headline">DELTA VAULT CENTER</h1>

    <div class="brand">
      <span class="brand-dot"></span>
      <span class="brand-name">LANTERN HOST</span>
    </div>

    <div class="tiles">
      <div class="tile tile--aisle" role="img" aria-label="Photo of a lit data center aisle with server cabinets"></div>
      <div class="tile tile--racks" role="img" aria-label="Photo of rows of server racks on a raised floor"></div>
      <div class="tile tile--cabling" role="img" aria-label="Photo of a technician working on network equipment"></div>
      <div class="tile tile--scanner" role="img" aria-label="Photo of a hand on a biometric security scanner"></div>
      <div class="tile tile--support"><span class="big">24/7</span><span class="small">SUPPORT</span></div>
    </div>

    <p class="features features--one">ON-SITE SUBDTATION<span class="sep"></span>REDUNDANT POWER<span class="sep"></span>COMPLETE EVIRONMENTAL CONTROL</p>
    <p class="features features--two">MULTI-HOMED BANDWIDTH<span class="sep"></span>ULTIMATE SECURITY<span class="sep"></span>24/7 SUPPORT</p>

    <svg class="offers-band" viewBox="0 0 745 258" aria-hidden="true">
      <defs>
        <linearGradient id="bandFill" x1="0" y1="0" x2="0" y2="1">
          <stop offset="0" stop-color="#2b2a2c"/>
          <stop offset="0.35" stop-color="#3a393b"/>
          <stop offset="1" stop-color="#323133"/>
        </linearGradient>
      </defs>
      <path d="M0 40 Q 372 -30 745 46 L745 258 L0 258 Z" fill="url(#bandFill)"/>
      <circle cx="342" cy="237" r="133" fill="#3f8f3f" opacity="0.55"/>
    </svg>

    <div class="offer offer--cloud">
      <p class="offer-title">PRIVATE CLOUD SERVER</p>
      <p class="offer-spec">24 VCPUS<span class="sep"></span>32 GB RAM</p>
      <p class="offer-spec">1TB RAID10 STORAGE</p>
      <p class="offer-spec">100MBPS</p>
      <p class="offer-price">$539/MO</p>
    </div>

    <div class="offer offer--colo">
      <p class="offer-title">COLOCATION</p>
      <p class="offer-spec">SPACE - 1U<span class="sep"></span>POWER - 1A@208V</p>
      <p class="offer-spec">PUBLIC NETWORK - 100MBPS</p>
      <p class="offer-spec">PRIVATE NETWORK - 1GBPS</p>
      <p class="offer-price">$89/MO</p>
    </div>
  </section>
</body>
</html>
```